Larchmere Hockey Academy

We are are Ice Hockey Development Company that provided on-ice Hockey development services. We need a Landing Page with tabs to direct to individual program pages.
Landing Page
About Page
Winter Program Page
Spring Program Page
Summer Program Page
Team Page
Tournament Page

```html
<!DOCTYPE html>
<html lang="en">
<head>
<meta charset="utf-8">
<title>Larchmere Hockey Academy</title>
<link href="https://fonts.googleapis.com/css2?family=Krona+One&family=Roboto:wght@400;500;700&family=Oswald:wght@400;500&display=swap" rel="stylesheet">
<style>
:root{
  --green:#2f9d2f;
  --green-dark:#0e6a12;
  --green-team:#34ae34;
  --black:#000;
  --white:#fff;
  --ink:#111;
  --grey:#666;
}
*{margin:0;padding:0;box-sizing:border-box}
html,body{width:1200px;height:3521px;overflow:hidden;background:var(--white)}
body{position:relative;font-family:"Roboto",sans-serif;color:var(--ink)}
.abs{position:absolute}
.display{font-family:"Krona One",sans-serif;text-transform:uppercase;letter-spacing:-0.5px}
.btn{position:absolute;display:flex;align-items:center;justify-content:center;font-family:"Krona One",sans-serif;font-size:13px;color:var(--white);text-transform:uppercase;background:linear-gradient(90deg,var(--green),var(--green-dark));letter-spacing:-0.3px}
.photo{position:absolute}

/* header */
.site-header{position:absolute;left:0;top:0;width:1200px;height:118px;background:var(--white)}
.brand{position:absolute;left:123px;top:34px;font-family:"Krona One",sans-serif;font-size:18px;line-height:24px;color:var(--ink)}
.call{left:849px;top:20px;width:235px;height:40px;font-size:15px}
.nav a{position:absolute;top:83px;font-size:12.5px;font-weight:500;color:var(--ink);text-decoration:none;letter-spacing:0.2px}

/* hero */
.hero{position:absolute;left:0;top:118px;width:1200px;height:671px;background:var(--black)}
.hero-photo{left:0;top:0;width:700px;height:671px;background:radial-gradient(ellipse at 45% 50%,#c8322c 0%,#5a1c26 30%,#1c2a44 55%,#000 80%)}
.hero-title{position:absolute;left:700px;top:178px;font-size:50px;line-height:64px;color:var(--white)}
.hero-btn{left:701px;top:386px;width:139px;height:52px}

/* about */
.about-frame{left:116px;top:1123px;width:161px;height:137px;border-left:11px solid var(--green);border-bottom:11px solid var(--green)}
.about-photo{left:135px;top:901px;width:387px;height:340px;background:linear-gradient(160deg,#6f9cc4,#c9dcec 60%,#e8f0f7)}
.about h2{position:absolute;left:579px;top:938px;font-size:30px}
.about p{position:absolute;left:579px;top:988px;width:436px;font-size:13px;line-height:19px;color:var(--grey)}
.about-btn{left:579px;top:1136px;width:138px;height:53px}

/* programs */
.programs-title{position:absolute;left:0;width:1200px;top:1393px;text-align:center;font-size:30px}
.program{position:absolute;top:1472px;width:399px;height:473px;overflow:hidden}
.program span{position:absolute;left:0;right:0;bottom:50px;text-align:center;font-family:"Krona One",sans-serif;font-size:21px;color:var(--white);text-transform:uppercase}
.p-winter{left:0;background:linear-gradient(180deg,#3d7fc4,#8fb3d6 45%,#3a4a66)}
.p-spring{left:400px;background:linear-gradient(180deg,#3f6fa8,#b3c3d3 45%,#4b4e58)}
.p-summer{left:801px;background:linear-gradient(180deg,#3c6b3a,#9fb06a 45%,#3f5a45)}

/* team */
.team{position:absolute;left:0;top:1948px;width:596px;height:548px;background:var(--green-team);color:var(--white)}
.team h2{position:absolute;left:149px;top:110px;font-size:30px}
.team p{position:absolute;left:149px;top:164px;width:380px;font-size:13.3px;line-height:19px}
.team-btn{left:152px;top:367px;width:139px;height:51px;background:transparent;border:2px solid var(--white)}
.team-photo{left:596px;top:1948px;width:604px;height:548px;background:linear-gradient(180deg,#5b7596,#c43a3a 55%,#d9dde2)}

/* tournament */
.tour-title{position:absolute;left:0;width:1200px;top:2606px;text-align:center;font-size:30px}
.tour-text{position:absolute;left:270px;width:660px;top:2656px;text-align:center;font-size:13px;line-height:19px;color:var(--grey)}
.player-left{left:150px;top:2747px;width:315px;height:358px;background:radial-gradient(ellipse at 45% 45%,#e8d27a,#f3f0e6 55%,#fff 75%)}
.player-right{left:820px;top:2747px;width:301px;height:358px;background:radial-gradient(ellipse at 40% 40%,#d8494a,#f2d6d6 55%,#fff 75%)}
.count{position:absolute;top:2748px;font-family:"Oswald",sans-serif;color:var(--green);text-align:center;width:80px}
.count b{display:block;font-weight:500;font-size:34px;line-height:40px}
.count i{display:block;font-style:normal;font-size:16px;line-height:22px}
.colon{position:absolute;top:2750px;font-family:"Oswald",sans-serif;font-size:30px;color:var(--green)}
.book-btn{left:530px;top:2862px;width:140px;height:51px}

/* footer */
.site-footer{position:absolute;left:0;top:3157px;width:1200px;height:364px;background:var(--black);color:var(--white)}
.foot-brand{position:absolute;left:0;width:1200px;top:84px;text-align:center;font-family:"Krona One",sans-serif;font-size:22px;line-height:28px}
.foot-col h4{position:absolute;top:190px;font-family:"Krona One",sans-serif;font-size:13px;font-weight:400}
.foot-col p{position:absolute;top:214px;font-size:13px;line-height:18px}
.divider{position:absolute;top:191px;width:1px;height:62px;background:#555}
.help-phone{font-family:"Krona One",sans-serif;font-size:19px!important;color:var(--green)}
.social{position:absolute;top:3382px;width:36px;height:36px;border-radius:50%;background:var(--white)}
.copy{position:absolute;left:0;width:1200px;top:3447px;text-align:center;font-size:13px;color:var(--white)}
</style>
</head>
<body>

<header class="site-header">
  <div class="brand">LARCHMERE<br>HOCKEY</div>
  <div class="btn call">Call_ 555 014 2760</div>
  <nav class="nav">
    <a style="left:379px">ABOUT</a>
    <a style="left:462px">WINTER PROGRAM</a>
    <a style="left:616px">SPRING PROGRAM</a>
    <a style="left:765px">SUMMER PROGRAM</a>
    <a style="left:924px">TEAM</a>
    <a style="left:994px">TOURNAMENT</a>
  </nav>
</header>

<section class="hero">
  <div class="photo hero-photo" role="img" aria-label="Hockey player in red jersey skating forward with stick, ice spray on dark background"></div>
  <h1 class="display hero-title">Larchmere<br>Hockey<br>Academy</h1>
  <div class="btn hero-btn">Read More</div>
</section>

<section class="about">
  <div class="abs about-frame"></div>
  <div class="photo about-photo" role="img" aria-label="Player skating toward goalie on an ice rink"></div>
  <h2 class="display">About Us</h2>
  <p>Lorem ipsum dolor sit amet, consectetur adipiscing elit, sed do eiusmod tempor incididunt ut labore et dolore magna aliqua. Quis ipsum suspe ndis se ultrices gravida. Risus commodo viverra maecenas accumsan lacus vel facilisis. Lorem ipsum dolor sit amet, consectetur adipiscing elit, sed do eiusmod tempor incididunt ut labore et dolore magna aliqua. Quis ipsum suspe ndisse ultrices gravida. Risus commodo viverra maecenas accum san lacus vel facilisis.</p>
  <div class="btn about-btn">Read More</div>
</section>

<section class="programs">
  <h2 class="display programs-title">Our Programs</h2>
  <div class="program p-winter" role="img" aria-label="Professional players battling for the puck in a lit arena"><span>Winter Program</span></div>
  <div class="program p-spring" role="img" aria-label="Young players in red and white facing off on ice"><span>Spring Program</span></div>
  <div class="program p-summer" role="img" aria-label="Field hockey players running on an outdoor pitch"><span>Summer Program</span></div>
</section>

<section class="team">
  <h2 class="display">Our Team</h2>
  <p>Lorem ipsum dolor sit amet, consectetur adipiscing elit, ed do eiusmod tempor incididunt ut labore et lore magna aliqualtrices graa. Quis ipsum suspe sse ultrices gravidorm ipsum dolor sit amet, consectetur adipiscing elit, sed do eiusmod tempor incididunt ut labore et lore magna aliquu ltrices graa. Quis ipsum suspe sse ultrices gravidsusLorem ipsum dolor sit amet, consectetur adipiscing elit, sed do eiusmod tempor incididunt ut labore et lore magna aliqu ultrices graa. Quis ipsum suspe sse ultrices gravids.</p>
  <div class="btn team-btn">Read More</div>
</section>
<div class="photo team-photo" role="img" aria-label="Youth team in red jerseys lined up on the ice with sticks"></div>

<section class="tournament">
  <h2 class="display tour-title">Tournament</h2>
  <p class="tour-text">Lorem ipsum dolor sit amet, consectetur adipiscing elit, sed do eiusmod tempor incididunt ut labore et dolore magna aliqua. Quis ipsum suspe ndisse ultrices gravida. Risus commodo viverra maecenas accumsan lacus vel facilisis. Lorem ipsum dolor sit amet, consectetur adipiscing elit, sed do eiusmod tempor</p>
  <div class="photo player-left" role="img" aria-label="Player in white and yellow kit handling the puck"></div>
  <div class="photo player-right" role="img" aria-label="Player in red kit skating with stick"></div>
  <div class="count" style="left:418px"><b>32</b><i>Days</i></div>
  <div class="colon" style="left:496px">:</div>
  <div class="count" style="left:516px"><b>28</b><i>Hours</i></div>
  <div class="colon" style="left:594px">:</div>
  <div class="count" style="left:606px"><b>54</b><i>Minutes</i></div>
  <div class="colon" style="left:684px">:</div>
  <div class="count" style="left:695px"><b>06</b><i>Seconds</i></div>
  <div class="btn book-btn">Book Now</div>
</section>

<footer class="site-footer">
  <div class="foot-brand">LARCHMERE<br>HOCKEY</div>
  <div class="foot-col">
    <h4 style="left:224px">ADDRESS</h4>
    <p style="left:224px">123&nbsp; Ipsum is simply dummy<br>text of theprintin</p>
    <h4 style="left:493px">NEED ANY HELP?</h4>
    <p class="help-phone" style="left:493px">(555) 0193 4482</p>
    <h4 style="left:794px">FOLLOW US</h4>
  </div>
  <div class="divider" style="left:452px"></div>
  <div class="divider" style="left:758px"></div>
</footer>
<div class="social" style="left:790px" aria-label="Social link"></div>
<div class="social" style="left:839px" aria-label="Social link"></div>
<div class="social" style="left:888px" aria-label="Social link"></div>
<div class="social" style="left:937px" aria-label="Social link"></div>
<p class="copy">© 2023 All Rights Reserved | Larchmere Hockey Academy.</p>

</body>
</html>
```